Business Card for bespoke luxury cupcakes and cakes
childrens parties, baby showers, seasonal designs, christenings, 3D and 2D designs
Bright & Fun-filled
Tumble Bakes Ltd
London
morvenaltoski@mailnest.co.uk
www.pagelink.co.uk/TumbleBakesLtd

```html
<!DOCTYPE html>
<html lang="en">
<head>
<meta charset="utf-8">
<title>Tumble Bakes Ltd – Business Card</title>
<link href="https://fonts.googleapis.com/css2?family=Comfortaa:wght@400;700&display=swap" rel="stylesheet">
<style>
  :root {
    --backdrop: #efede8;
    --card: #ffffff;
    --brand-pink: #e8559b;
    --magenta: #a3206b;
    --magenta-deep: #c0186e;
    --sky: #2aa6df;
    --orange: #f39a2d;
    --green: #7cc242;
    --purple: #8e4fa3;
    --soft-pink: #f7c9dc;
    --white: #ffffff;
  }
  html, body {
    margin: 0;
    width: 1200px;
    height: 828px;
    overflow: hidden;
    background: var(--backdrop);
  }
  .card {
    position: absolute;
    left: 50px;
    top: 94px;
    width: 1100px;
    height: 640px;
    border-radius: 28px;
    background: var(--card);
    overflow: hidden;
    box-shadow: 0 4px 14px rgba(0,0,0,0.12);
  }
  .dot-field {
    position: absolute;
    left: 0; top: 0;
    width: 1100px; height: 470px;
    background: radial-gradient(ellipse at 50% 40%, #f6e9ec 0%, #fbf3f1 55%, #ffffff 100%);
  }
  .phone-tag {
    position: absolute;
    right: 0; top: 0;
    width: 340px; height: 68px;
    background: var(--sky);
    color: var(--white);
    font: 400 32px/68px "Comfortaa", sans-serif;
    text-align: center;
    letter-spacing: 1px;
  }
  .mascot {
    position: absolute;
    left: 40px; top: 70px;
    width: 170px; height: 210px;
    border-radius: 40%;
    background: radial-gradient(circle at 50% 40%, #fde6c8 0%, #f6b6cf 70%, #f4a3c4 100%);
  }
  .business-name {
    position: absolute;
    left: 235px; top: 110px;
    margin: 0;
    font: 700 88px/104px "Comfortaa", sans-serif;
    color: var(--brand-pink);
  }
  .business-name span { display: block; }
  .flower-art {
    position: absolute;
    left: 760px; top: 100px;
    width: 320px; height: 370px;
    border-radius: 30px;
    background: linear-gradient(160deg, #fbe4b0 0%, #f3c0d9 40%, #cbe6a8 70%, #d6c2e6 100%);
    opacity: 0.85;
  }
  .contact-band {
    position: absolute;
    left: 0; top: 372px;
    width: 640px; height: 118px;
    background: var(--magenta);
    color: var(--white);
    box-sizing: border-box;
    padding: 14px 0 0 48px;
  }
  .contact-band .email {
    font: 400 34px/50px "Comfortaa", sans-serif;
    white-space: nowrap;
  }
  .contact-band .web {
    font: 400 19px/30px "Comfortaa", sans-serif;
    color: var(--soft-pink);
    margin-left: 80px;
    white-space: nowrap;
  }
  .stripe-band {
    position: absolute;
    left: 0; top: 490px;
    width: 1100px; height: 150px;
    background: linear-gradient(180deg, #fbd9b0 0%, var(--orange) 25%, var(--green) 45%, var(--purple) 62%, var(--magenta-deep) 80%, var(--magenta-deep) 100%);
  }
</style>
</head>
<body>
  <div class="card">
    <div class="dot-field" role="img" aria-label="Soft pastel polka dot pattern"></div>
    <div class="phone-tag">+44-7700-900-412</div>
    <div class="mascot" role="img" aria-label="Cartoon cherub holding a cupcake"></div>
    <h1 class="business-name"><span>Tumble</span><span>Bakes</span></h1>
    <div class="flower-art" role="img" aria-label="Colourful swirl lollipop flowers with a butterfly"></div>
    <div class="contact-band">
      <div class="email">morvenaltoski@mailnest.co.uk</div>
      <div class="web">www.pagelink.co.uk/TumbleBakesLtd</div>
    </div>
    <div class="stripe-band" role="img" aria-label="Decorative multicolour stripe band with stitched lines"></div>
  </div>
</body>
</html>
```